NEW Household Invention Needs a Package Design!

We need a 'retail' package design for a new product invented for the household kitchen market. Tiverlyn has developed a reusable food storage system that can be tailored to an individual's needs and have a sustainable impact on their ability to make good dietary decisions, while helping save the planet. We would like to see designs that use the brand's branding guidelines and logo. The final design should communicate the key features of the product (patented customizable modular system, fill lines, collapsible functionality and sustainable materials), as well as, all other notable aspects (Microwave/Dishwasher Safe, Leakproof, 100% BPA Free, Donates 1% of purchase price, etc.). It's important that the benefits of the product are well highlighted (More variety to better balance nutrition, More easily stored in bag, kitchen cabinet or drawer and Ends waste)
Updates

Hi All, we are looking for a package design for retail, something that will be on a shelf in our product category.

Need extra days to review

Target Market(s)

Health conscious men and women who have a passion for nutrition & social responsibility, operate a lifestyle on-the-go and monitor their spending by preparing meals at home.

Industry/Entity Type

Food Tech, Consumer Products, Health & Wellness

Font styles to use
Other font styles liked:
• See Brand Guidelines

Requirements
Must have
• Follow brand guidelines: https://guidelines.morbexcreative.com/tiverlyn/guidelines/

```html
<!DOCTYPE html>
<html lang="en">
<head>
<meta charset="utf-8">
<title>Tiverlyn – The Vessa container set packaging</title>
<link rel="stylesheet" href="https://fonts.googleapis.com/css2?family=Archivo:wght@400;600;700;800&display=swap">
<style>
:root{
  --kraft:#C9B08E;
  --kraft-dark:#BFA583;
  --ink:#2b2b2b;
  --white:#ffffff;
  --sky:#A9DAF3;
  --sky-deep:#7CC4EA;
  --plum:#8B1E66;
  --veg-red:#C8243A;
  --veg-purple:#6E2A6B;
  --veg-orange:#E9772E;
  --coral:#E8585A;
}
*{margin:0;padding:0;box-sizing:border-box}
html,body{width:1200px;height:4454px;overflow:hidden;background:#fff}
body{font-family:"Archivo",Arial,sans-serif;color:var(--white);position:relative}
.dieline{position:absolute;left:74px;top:29px;width:1056px;height:4341px;background:var(--kraft);border:2px solid var(--ink)}
.fold{position:absolute;left:74px;width:1056px;height:0;border-top:2px solid var(--ink)}
.abs{position:absolute}
.brand{font-weight:700;letter-spacing:-1px;line-height:1}
.title{font-weight:800;line-height:1;letter-spacing:-1px}
.subtitle{font-weight:700;line-height:1}
.copy{font-weight:600;line-height:1.3}
.photo{left:74px;top:1056px;width:1056px;height:745px;background:linear-gradient(160deg,var(--sky) 0%,#BFE4F6 45%,var(--sky-deep) 100%)}
.seal{width:248px;height:248px;border-radius:50%;background:var(--plum);display:flex;align-items:center;justify-content:center;font-weight:700;font-size:46px}
.features{display:flex;gap:28px}
.feature{width:126px;height:214px;border:2px solid var(--white);border-radius:12px;display:flex;flex-direction:column;overflow:hidden}
.feature .icon{height:106px;border-bottom:2px solid var(--white);display:flex;align-items:center;justify-content:center}
.feature .label{flex:1;display:flex;align-items:center;justify-content:center;text-align:center;font-size:17px;font-weight:600;line-height:1.25;padding:0 6px}
.features.small{gap:29px}
.pledge{left:605px;top:2570px;width:444px;height:110px;background:var(--white);border-radius:14px;display:flex;align-items:center;gap:22px;padding:0 22px;color:var(--kraft);font-weight:700;font-size:19px;line-height:1.2}
.specs{left:624px;top:2950px;font-weight:700;font-size:26px;line-height:1.12}
.specs p{margin-bottom:24px;font-size:23px;line-height:1.2}
.drawing{left:830px;top:3060px;width:206px;height:118px;border-radius:10px;background:rgba(255,255,255,.18)}
.illustration{left:275px;top:3337px;width:757px;height:330px;border-radius:24px;background:linear-gradient(90deg,var(--veg-red) 0%,var(--veg-purple) 55%,var(--veg-orange) 80%,var(--coral) 100%);opacity:.85}
.rule{height:0;border-top:2px solid var(--white);left:148px;width:901px}
.code-area{left:743px;top:4035px;width:317px;height:155px;background:var(--white)}
.vline{left:597px;top:4068px;width:0;height:232px;border-left:2px solid var(--white)}
</style>
</head>
<body>
<div class="dieline"></div>
<div class="fold" style="top:320px"></div>
<div class="fold" style="top:2200px"></div>
<div class="fold" style="top:2489px"></div>

<!-- Front panel -->
<div class="abs brand" style="left:134px;top:395px;font-size:128px">tiverlyn</div>
<div class="abs title" style="left:148px;top:757px;font-size:112px">The Vessa</div>
<div class="abs subtitle" style="left:148px;top:876px;font-size:46px">container set</div>
<div class="abs copy" style="left:148px;top:938px;font-size:25px">The ideal lunchbox for the on-the-go lifestyle.<br>Pack a balanced meal, perfectly portioned.</div>

<div class="abs photo" role="img" aria-label="Photo of three collapsible sky-blue containers with clear lids holding crispbread, tomato, egg and a sprout salad"></div>
<div class="abs seal" style="left:801px;top:932px">tiverlyn</div>

<div class="abs features" style="left:609px;top:1911px">
  <div class="feature"><div class="icon"><svg width="78" height="46" viewBox="0 0 78 46" fill="none" stroke="#fff" stroke-width="2"><rect x="1" y="1" width="76" height="44" rx="3"/><rect x="8" y="8" width="46" height="30" rx="2"/><line x1="60" y1="8" x2="60" y2="38"/><circle cx="66" cy="12" r="2"/><circle cx="72" cy="12" r="2"/></svg></div><div class="label">Microwave/<br>Dishwasher<br>Safe</div></div>
  <div class="feature"><div class="icon"><svg width="70" height="70" viewBox="0 0 70 70" fill="none" stroke="#fff" stroke-width="2"><path d="M24 18c6 10 10 16 10 22a10 10 0 0 1-20 0c0-6 4-12 10-22z"/><path d="M46 38c4 7 6 10 6 14a6 6 0 0 1-12 0c0-4 2-7 6-14z"/><line x1="10" y1="62" x2="64" y2="8"/></svg></div><div class="label">Leakproof</div></div>
  <div class="feature"><div class="icon"><svg width="56" height="56" viewBox="0 0 56 56" fill="none" stroke="#fff" stroke-width="2"><path d="M8 48C8 22 24 8 50 6c0 28-14 42-40 42z"/><line x1="8" y1="48" x2="38" y2="18"/></svg></div><div class="label">100%<br>BPA<br>Free</div></div>
</div>

<!-- Back panel -->
<div class="abs pledge"><svg width="70" height="62" viewBox="0 0 70 62" fill="none" stroke="#C9B08E" stroke-width="3"><path d="M35 58C8 40 2 28 2 18A16 16 0 0 1 35 12a16 16 0 0 1 33 6c0 10-6 22-33 40z"/></svg><span>WITH EVERY CONTAINER SOLD, 1% OF THE PURCHASE PRICE WILL BE DONATED TO THE ASSOCIATED CHARITY.</span></div>

<div class="abs brand" style="left:148px;top:2712px;font-size:116px">tiverlyn</div>
<div class="abs title" style="left:148px;top:2872px;font-size:74px">The Vessa</div>
<div class="abs subtitle" style="left:148px;top:2950px;font-size:41px">container set</div>
<div class="abs copy" style="left:148px;top:2998px;font-size:23px;width:440px">The ideal lunchbox for the on-the-go lifestyle. Pack a balanced meal, perfectly portioned.</div>
<div class="abs copy" style="left:148px;top:3132px;font-size:23px;width:450px">Terrific for salads, pastas, stews, there are no limits. Pack your favorite balanced meal with this perfectly portioned food storage container set. Then collapse and stow away for a more convenient carrying size.</div>

<div class="abs specs">
  <div style="margin-bottom:42px">6 Pieces | 1 Utensil<br>3 Compartment</div>
  <p>Large Compartment<br>Volume<br>24oz<br>709.8ml</p>
  <p>Small Compartments<br>Volume<br>8oz<br>236.7ml</p>
</div>
<div class="abs drawing" role="img" aria-label="Line drawing of the three-compartment container set"></div>

<div class="abs illustration" role="img" aria-label="Illustration of a container outline holding a red pepper, a beetroot and a carrot, with a coral brand badge"></div>

<div class="abs rule" style="top:3702px"></div>
<div class="abs features small" style="left:153px;top:3738px">
  <div class="feature"><div class="icon"><svg width="70" height="44" viewBox="0 0 78 46" fill="none" stroke="#fff" stroke-width="2"><rect x="1" y="1" width="76" height="44" rx="3"/><rect x="8" y="8" width="46" height="30" rx="2"/><line x1="60" y1="8" x2="60" y2="38"/></svg></div><div class="label">Microwave<br>Safe</div></div>
  <div class="feature"><div class="icon"><svg width="50" height="62" viewBox="0 0 50 62" fill="none" stroke="#fff" stroke-width="2"><rect x="1" y="1" width="48" height="60" rx="3"/><line x1="1" y1="14" x2="49" y2="14"/><circle cx="25" cy="36" r="13"/></svg></div><div class="label">Dishwasher<br>Safe</div></div>
  <div class="feature"><div class="icon"><svg width="60" height="60" viewBox="0 0 60 60" fill="none" stroke="#fff" stroke-width="2"><rect x="1" y="1" width="58" height="58" rx="3"/><line x1="30" y1="16" x2="30" y2="50"/><line x1="15" y1="24" x2="45" y2="42"/><line x1="45" y1="24" x2="15" y2="42"/></svg></div><div class="label">Freezer<br>Safe</div></div>
  <div class="feature"><div class="icon"><svg width="66" height="44" viewBox="0 0 66 44" fill="none" stroke="#fff" stroke-width="2"><rect x="1" y="10" width="64" height="32" rx="4"/><rect x="6" y="2" width="54" height="10" rx="3"/><line x1="33" y1="10" x2="33" y2="42"/></svg></div><div class="label">Airlight</div></div>
  <div class="feature"><div class="icon"><svg width="64" height="64" viewBox="0 0 70 70" fill="none" stroke="#fff" stroke-width="2"><path d="M24 18c6 10 10 16 10 22a10 10 0 0 1-20 0c0-6 4-12 10-22z"/><path d="M46 38c4 7 6 10 6 14a6 6 0 0 1-12 0c0-4 2-7 6-14z"/><line x1="10" y1="62" x2="64" y2="8"/></svg></div><div class="label">Leakproof</div></div>
  <div class="feature"><div class="icon"><svg width="50" height="50" viewBox="0 0 56 56" fill="none" stroke="#fff" stroke-width="2"><path d="M8 48C8 22 24 8 50 6c0 28-14 42-40 42z"/><line x1="8" y1="48" x2="38" y2="18"/></svg></div><div class="label">100%<br>BPA<br>Free</div></div>
</div>
<div class="abs rule" style="top:4022px"></div>
<div class="abs vline"></div>
<div class="abs code-area"></div>
</body>
</html>
```